WordPress Website Design & Theme - The Meridian Bidding House

Need a WordPress design for an auction company wanting a responsive, simple and easy to use site.

Please keep in mind that the design will be built on a responsive WP theme.

Colors will be light or white and complimentary/highlight colors from the logo.

Industry/Entity Type

It Company

Number of Pages Required

1 page

Font styles to use
Serif
Sans Serif

Requirements
Must have
• Navigation - 1) Home 2) Auction Calendar 3) Auction Results 4) For Sale 5) Services 6)About Us 7) Contact Us
• A site they mention liking is http://www.quillenbidhall.example/
• Site will have full width slideshow 960px. Use stock real estate photo. Header will have logo (attached) and contact info:
• THE MERIDIAN BIDDING HOUSE
• P.O. Box 862
• Gadsden, AL 35917
• PHONE: (800)615-8840 or (256)382-9017
• FAX: (541)382-6651
• EMAIL: info@meridian-bidding.example
• There will be no sidebar on the homepage. There can be 3 horizontal widgets for "featured Listings", Join Our Newsletter, and maybe a form like http://www.meridian-bidding.example/request_proposal.php. The "Upcoming Auctions" feature as is seen on http://www.quillenbidhall.example/ will be used (attached image).
• In the footer: contact info, social media (FB, twitter, RSS), affiliation logos (attached), perhaps smaller company logo, News & Events blog, and if room "Featured Auctions".
Nice to have
• Use of drop-down menus styling- 1) Live Auctions 2) Online Auctions - under the Auction Calendar tab

```html
<!DOCTYPE html>
<html lang="en">
<head>
<meta charset="utf-8">
<title>The Meridian Bidding House</title>
<link rel="stylesheet" href="https://fonts.googleapis.com/css2?family=Open+Sans:wght@400;600;700&display=swap">
<style>
:root{
  --red:#d3223c;
  --red-dark:#b8152c;
  --navy:#2e2a55;
  --ink:#333;
  --muted:#8a8a8a;
  --line:#e2e2e2;
  --page:#f2f2f2;
  --footer:#333333;
  --footer-bottom:#262626;
  --link:#1a56a8;
}
*{box-sizing:border-box;margin:0;padding:0}
html,body{width:1200px;height:2258px;overflow:hidden}
body{position:relative;font-family:"Open Sans",Arial,sans-serif;color:var(--ink);background:var(--page)}
.abs{position:absolute}

/* header */
.header{left:0;top:0;width:1200px;height:104px;background:#fff;border-top:3px solid var(--red)}
.brand{left:102px;top:22px;display:flex;align-items:center;gap:10px}
.brand-dot{width:56px;height:56px;border-radius:50%;background:var(--red)}
.brand-name{font-size:17px;font-weight:700;color:var(--red);line-height:1.15;width:130px}
.contact-item{top:32px;display:flex;gap:14px;font-size:13px;font-weight:600;color:#444;line-height:23px}
.icon-ring{width:38px;height:38px;border-radius:50%;border:2px solid #d6d6e0;display:flex;align-items:center;justify-content:center;flex:none}
.nav{left:0;top:104px;width:1200px;height:62px;background:linear-gradient(var(--red),var(--red-dark))}
.nav a{position:absolute;top:21px;font-size:14px;font-weight:600;color:#fff;text-decoration:none}
.caret{display:inline-block;border:4px solid transparent;border-top-color:#fff;margin-left:3px;vertical-align:middle}

/* slider */
.slider{left:104px;top:206px;width:992px;height:472px;background:#fff;border:1px solid var(--line);padding:5px}
.slide-photo{width:100%;height:100%;background:linear-gradient(180deg,#1f5fc4 0%,#6a9ad6 45%,#c9c7bd 70%,#5d7a3e 100%)}
.slider-arrow{top:465px;width:16px;height:16px;border-right:3px solid #fff;border-bottom:3px solid #fff}

/* widgets */
.widget{top:732px;height:503px;background:#fff;border:1px solid var(--line);box-shadow:0 14px 12px -12px rgba(0,0,0,.25)}
.widget-title{height:48px;color:#fff;font-size:19px;font-weight:600;text-align:center;line-height:48px}
.title-red{background:linear-gradient(var(--red),var(--red-dark))}
.title-navy{background:linear-gradient(#3b3668,var(--navy))}
.listing{position:absolute;left:16px;display:flex;gap:14px;width:290px}
.listing-thumb{width:68px;height:60px;border:2px solid #ddd;flex:none}
.listing h3{font-size:17px;font-weight:600;color:var(--link);margin-top:6px}
.listing p{font-size:14px;font-weight:700;color:#333;text-decoration:underline;margin-top:2px}
.listing-rule{position:absolute;left:16px;width:290px;border-top:1px solid var(--line)}
.more-dot{right:16px;bottom:18px;width:18px;height:18px;border-radius:50%;background:var(--navy)}
.news-text{left:22px;top:68px;width:280px;font-size:14px;line-height:28px;color:#777;text-align:justify}
.field{position:absolute;border:1px solid #ddd;background:#fff;font-size:14px;color:#aaa;padding:0 14px;display:flex;align-items:center}
.btn{position:absolute;background:var(--red);color:#fff;font-size:17px;font-weight:600;border-radius:3px;text-align:center}
.captcha-label{font-size:14px;color:#555}

/* upcoming */
.upcoming{left:0;top:1303px;width:1200px;height:569px;background:linear-gradient(180deg,#5f7ea8 0%,#a2a9a8 40%,#8b8a7e 70%,#5c6a3a 100%)}
.upcoming h2{position:absolute;left:0;top:62px;width:1200px;text-align:center;color:#fff;font-size:25px;font-weight:600}
.card{position:absolute;background:#fff;box-shadow:0 2px 10px rgba(0,0,0,.3)}
.card-photo{position:absolute}
.card-date{position:absolute;color:#fff;font-weight:700;text-align:center}
.up-arrow{top:1630px;width:16px;height:16px;border-right:3px solid #fff;border-bottom:3px solid #fff}

/* footer */
.footer{left:0;top:1872px;width:1200px;height:301px;background:var(--footer);color:#ccc}
.footer h4{position:absolute;top:44px;font-size:18px;font-weight:600;color:#fff}
.badge{position:absolute;background:#e9e9e9}
.post{position:absolute;left:334px;width:270px;font-size:14px;line-height:22px;color:#ddd;padding-left:22px}
.post::before{content:"»";position:absolute;left:0;top:0;color:#fff}
.post small{color:#3b8ede;font-size:11px;text-decoration:underline}
.f-contact{position:absolute;left:649px;display:flex;gap:14px;font-size:14px;line-height:22px;color:#bbb}
.social{position:absolute;top:100px;width:46px;height:46px;border-radius:50%;border:2px solid #fff}
.copyright{left:0;top:2173px;width:1200px;height:85px;background:var(--footer-bottom);color:#fff;font-size:15px;text-align:center;line-height:85px}
</style>
</head>
<body>

<header class="abs header">
  <div class="abs brand"><span class="brand-dot"></span><span class="brand-name">The Meridian Bidding House</span></div>
  <div class="abs contact-item" style="left:478px">
    <span class="icon-ring"><svg width="16" height="16" viewBox="0 0 24 24"><path fill="#2e2a55" d="M6.6 10.8a15 15 0 0 0 6.6 6.6l2.2-2.2a1 1 0 0 1 1-.25 11 11 0 0 0 3.6.6 1 1 0 0 1 1 1V20a1 1 0 0 1-1 1A17 17 0 0 1 3 4a1 1 0 0 1 1-1h3.5a1 1 0 0 1 1 1 11 11 0 0 0 .6 3.6 1 1 0 0 1-.25 1z"/></svg></span>
    <span>- &nbsp;PHONE : (888)615-8840 (or)<br>(541)382-9017</span>
  </div>
  <div class="abs contact-item" style="left:776px">
    <span class="icon-ring"><svg width="14" height="18" viewBox="0 0 14 20"><path fill="#2e2a55" d="M7 0a7 7 0 0 0-7 7c0 5 7 13 7 13s7-8 7-13a7 7 0 0 0-7-7zm0 9.5A2.5 2.5 0 1 1 7 4.5a2.5 2.5 0 0 1 0 5z"/></svg></span>
    <span>The Meridian Bidding House , Harlow<br>Springs OR 97419 , P.O. Box 862</span>
  </div>
</header>

<nav class="abs nav">
  <a style="left:289px">Home</a>
  <a style="left:370px">Auction<span class="caret"></span></a>
  <a style="left:467px">Calendar</a>
  <a style="left:571px">Auction Results</a>
  <a style="left:720px">For Sale</a>
  <a style="left:816px">Services</a>
  <a style="left:916px">About Us</a>
  <a style="left:1021px">Contact Us</a>
</nav>

<section class="abs slider">
  <div class="slide-photo" role="img" aria-label="Two-storey suburban house with white garage under a blue sky"></div>
</section>
<span class="abs slider-arrow" style="left:136px;transform:rotate(135deg)"></span>
<span class="abs slider-arrow" style="left:1052px;transform:rotate(-45deg)"></span>

<section class="abs widget" style="left:104px;width:322px">
  <div class="widget-title title-red">Featured Listings</div>
  <div class="listing" style="top:74px"><span class="listing-thumb" role="img" aria-label="Small plant in hand" style="background:linear-gradient(#dfe8c0,#7fa23a)"></span><div><h3>Ne veritus complectitur</h3><p>listing-house.example</p></div></div>
  <span class="listing-rule" style="top:152px"></span>
  <div class="listing" style="top:178px"><span class="listing-thumb" role="img" aria-label="Green growth concept" style="background:linear-gradient(#e8f0c8,#8cbf3a)"></span><div><h3>Qui et quaeque habem</h3><p>listing-house.example</p></div></div>
  <span class="listing-rule" style="top:256px"></span>
  <div class="listing" style="top:282px"><span class="listing-thumb" role="img" aria-label="Office towers" style="background:linear-gradient(#4f86c6,#2a4e7c)"></span><div><h3>Duo no oblique</h3><p>listing-house.example</p></div></div>
  <span class="listing-rule" style="top:360px"></span>
  <div class="listing" style="top:386px"><span class="listing-thumb" role="img" aria-label="Commercial building" style="background:linear-gradient(#8fb8e8,#b88a64)"></span><div><h3>Virtute patrioque id nam</h3><p>listing-house.example</p></div></div>
  <span class="abs more-dot"></span>
</section>

<section class="abs widget" style="left:440px;width:322px">
  <div class="widget-title title-navy">Newsletter Signup</div>
  <p class="abs news-text"><svg width="20" height="14" viewBox="0 0 20 14" style="vertical-align:-1px;margin-right:10px"><rect width="20" height="14" fill="#d3223c"/><path d="M0 0l10 8 10-8" fill="none" stroke="#fff" stroke-width="1.5"/></svg>Nam ea nusquam pericula Meanus Virtute patrioque id nam, fugit inani vocent et vix. Qui et quaeque habemus rationibus, est labitur bonorum copiosae ut, has abhorreant accommodare interpretaris ne. His an sint esse, mazim saepe periculis usu ne</p>
  <div class="field" style="left:21px;top:292px;width:278px;height:44px">Email</div>
  <div class="field" style="left:21px;top:350px;width:278px;height:44px">Name</div>
  <div class="btn" style="left:90px;top:422px;width:134px;height:40px;line-height:40px">Subscribe</div>
</section>

<section class="abs widget" style="left:776px;width:323px">
  <div class="widget-title title-red">Submission Form</div>
  <div class="field" style="left:30px;top:74px;width:262px;height:42px">Name</div>
  <div class="field" style="left:30px;top:124px;width:262px;height:42px">Email</div>
  <div class="field" style="left:30px;top:174px;width:262px;height:42px">Phone</div>
  <div class="field" style="left:30px;top:224px;width:262px;height:86px;align-items:flex-start;padding-top:10px">Property Description</div>
  <div class="abs captcha-label" style="left:30px;top:322px">Enter the Words Below</div>
  <div class="field" style="left:30px;top:350px;width:220px;height:38px;color:#111;font-size:22px;font-weight:700">flextime</div>
  <span class="abs" style="left:268px;top:350px;width:18px;height:40px;background:#3a7bd5;border-radius:3px"></span>
  <div class="field" style="left:30px;top:394px;width:262px;height:36px"></div>
  <div class="abs" style="left:176px;top:456px;font-size:15px;font-weight:600;color:var(--red);text-decoration:underline">Submit</div>
  <div class="abs" style="left:250px;top:456px;font-size:15px;color:#333">Reset</div>
</section>

<section class="abs upcoming" role="img" aria-label="Large warehouse building under a blue sky, behind the auction cards">
  <h2>Upcoming Auctions</h2>
  <div class="card" style="left:197px;top:192px;width:240px;height:270px">
    <span class="card-photo" role="img" aria-label="Digital house model" style="left:30px;top:28px;width:186px;height:156px;background:linear-gradient(#0f3a7a,#2a7ad8)"></span>
    <div class="card-date" style="left:30px;top:184px;width:186px;height:52px;line-height:52px;font-size:19px;background:var(--navy)">Feb 18 , 2016</div>
  </div>
  <div class="card" style="left:762px;top:192px;width:241px;height:270px">
    <span class="card-photo" role="img" aria-label="Small house on grass held in a hand" style="left:26px;top:28px;width:186px;height:156px;background:linear-gradient(#e9ecef,#9fc34a)"></span>
    <div class="card-date" style="left:26px;top:184px;width:186px;height:52px;line-height:52px;font-size:19px;background:var(--navy)">Feb 18 , 2016</div>
  </div>
  <div class="card" style="left:438px;top:152px;width:322px;height:358px">
    <span class="card-photo" role="img" aria-label="Couple reviewing documents with an agent" style="left:40px;top:32px;width:246px;height:208px;background:linear-gradient(#cfe3ee,#b89a82)"></span>
    <div class="card-date" style="left:40px;top:240px;width:246px;height:66px;line-height:66px;font-size:24px;font-weight:600;background:var(--red)">Feb 18 , 2016</div>
  </div>
</section>
<span class="abs up-arrow" style="left:130px;transform:rotate(135deg)"></span>
<span class="abs up-arrow" style="left:1058px;transform:rotate(-45deg)"></span>

<footer class="abs footer">
  <h4 style="left:102px">AFFILATED LOGOS</h4>
  <span class="badge" style="left:104px;top:102px;width:48px;height:48px"></span>
  <span class="badge" style="left:200px;top:102px;width:62px;height:54px"></span>
  <span class="badge" style="left:152px;top:190px;width:60px;height:60px;border-radius:50%"></span>

  <h4 style="left:334px">LATEST POST</h4>
  <p class="post" style="top:90px">Legere voluptua id mea, nostrum suavitate nam eu. <small>Before 2 days</small></p>
  <p class="post" style="top:156px">Legere voluptua id mea, nostrum suavitate nam eu. <small>Before 3 days</small></p>

  <h4 style="left:649px">CONTACT US</h4>
  <div class="f-contact" style="top:90px"><svg width="16" height="14" viewBox="0 0 16 14"><path fill="#fff" d="M8 0l8 7h-2v7h-4V9H6v5H2V7H0z"/></svg><span>The Meridian Bidding House ,<br>Harlow Springs, OR 97419<br>P.O. Box 862</span></div>
  <div class="f-contact" style="top:174px"><svg width="16" height="20" viewBox="0 0 12 20"><rect x="1" y="1" width="10" height="18" rx="2" fill="none" stroke="#fff" stroke-width="2"/></svg><span>Call Us : (541)555-0142</span></div>
  <div class="f-contact" style="top:214px"><svg width="16" height="14" viewBox="0 0 20 14"><rect x="1" y="1" width="18" height="12" fill="none" stroke="#fff" stroke-width="2"/><path d="M1 1l9 7 9-7" fill="none" stroke="#fff" stroke-width="2"/></svg><span>info@meridian-bidding.example</span></div>
  <div class="f-contact" style="top:252px"><svg width="16" height="16" viewBox="0 0 16 16"><rect x="1" y="4" width="14" height="11" fill="#fff"/><rect x="4" y="0" width="8" height="5" fill="#fff"/></svg><span>Fax : (541)382-6651</span></div>

  <h4 style="left:928px">CONNECT US WITH</h4>
  <span class="social" style="left:938px"></span>
  <span class="social" style="left:995px"></span>
  <span class="social" style="left:1052px"></span>
</footer>
<div class="abs copyright">© &nbsp;Companyname 2016 . All Rights Reserved</div>

</body>
</html>
```